Grafitti Inspired Underwear Brand Needs Website

Rex's Briefs needs a website concept for our upcoming ecommerce site. Rex’s Briefs is an underwear line targeting a male demographic between 16 and 25. The logo is in the attachments. The brand is a colorful, rebellious underwear brand targeting men who are all about getting noticed and having a good time. And especially about meeting women. We need a website concept than will transport the audience into a world of rebellion, color and fun. We are totally open to ideas, but our initial thought is its an urban, graffiti jungle. It should be a transportive web environment that will make the audience feel they are entering this other world. It could be a street setting or it could be an alleyway (googling grafitti alleyway gives some ideas) or something else.

One challenge will be to create this colorful setting against which the various navigation tabs and product pictures will stand out in such a way as to allow easy e-commerce. Maybe the setting could be a building or garage with windows that the tabs would be set against for visibility.

Here is something we really like, but we have no idea how to make the various navigation tabs visible against a background as colorful and varied as this.

http://tapestrynook.example/w/Zk7pR2m

The brand is based on colorful and edgy designs that may certainly be provocative and even sexist in some minds. Similar brands are Tornavelo and Sven Lakso (before the went unisex fitness.) Please visit those brand sites to get an idea of what the product will look like.

From an executional perspective, the primary navigation tabs are in the attached map.

Again, this is an ecommerce site so saleable product must be easily visible on the homepage and elsewhere. The basic structure should be pretty standard with Hero A’s, Hero B’s, product shots and promotion boxes all very visible, but what we need is a really cool environment concept.

Primary navigation tabs should be horizontal across the top of the site in a pretty standard fashion and are:

1. Dangerous Rex’s
2. Wild Rex’s
3. Plain Rex’s
4. All the Damn Rex’s
5. Design Rex’s
6. Rex’s Life
7. Rex’s Jokes
8. About Rex’s

Target Market(s)

Men 16-25

Number of Pages Required

1 page

Requirements
Must have
• Brand Logo.
Nice to have
• Fun use of the devil/heart logo

```html
<!DOCTYPE html>
<html lang="en">
<head>
<meta charset="utf-8">
<title>Rex's Briefs — Home</title>
<link rel="stylesheet" href="https://fonts.googleapis.com/css2?family=Open+Sans:wght@400;600;700&display=swap">
<style>
:root{
  --purple:#6b2d8f;
  --lime:#8dc63f;
  --ink:#333;
  --muted:#666;
  --line:#e2e2e2;
  --topbar:#f1f1f1;
  --footer:#f4f4f4;
  --dark:#3a3a3a;
  --ghost:#e4e4e4;
}
*{box-sizing:border-box;margin:0;padding:0}
html,body{width:890px;height:1200px;overflow:hidden;background:#fff}
body{position:relative;font-family:'Open Sans',Arial,sans-serif;color:var(--ink)}
.abs{position:absolute}

/* top bar */
.topbar{left:0;top:0;width:890px;height:30px;background:var(--topbar)}
.phone{left:100px;top:6px;font-size:12px;color:var(--muted);display:flex;align-items:center;gap:5px}
.util{right:98px;top:6px;display:flex;align-items:center;gap:14px}
.cart-label{font-size:7px;line-height:8px;color:var(--muted);text-align:left}

/* header */
.header{left:0;top:30px;width:890px;height:106px;border-bottom:1px solid var(--line)}
.brand{left:0;width:890px;top:62px;text-align:center;display:flex;justify-content:center;align-items:center;gap:8px}
.brand-dot{width:26px;height:26px;border-radius:50%;background:var(--lime)}
.brand-name{font-size:26px;font-weight:700;color:var(--purple)}
.figure{background:linear-gradient(180deg,var(--ghost),#f3f3f3);border-radius:40px 40px 20px 20px;opacity:.8}

/* nav */
.nav{left:98px;top:156px;width:694px;display:flex;justify-content:space-between;font-size:8.6px;color:#555}
.nav .current{color:var(--purple)}

/* hero */
.hero{left:0;top:191px;width:890px;height:264px;background:linear-gradient(100deg,#d84a1c 0%,#3b2a6e 22%,#e58a1e 45%,#c23c2a 58%,#4b35a8 75%,#2a2a7a 100%)}
.hero-title{left:214px;top:287px;width:462px;height:34px;background:rgba(0,0,0,.55);color:#fff;font-size:20px;font-weight:600;text-align:center;line-height:34px}
.hero-cta{left:401px;top:328px;width:88px;height:31px;background:var(--lime);color:#fff;font-size:12px;font-weight:700;text-align:center;line-height:31px;letter-spacing:.3px}
.hero-arrow{top:311px;width:18px;height:22px;background:rgba(0,0,0,.45);display:flex;align-items:center;justify-content:center}

/* products */
.section-head{left:0;width:890px;top:509px;display:flex;justify-content:center;align-items:center;gap:16px}
.section-title{font-size:18px;font-weight:600;letter-spacing:.5px;color:#222}
.pager{width:17px;height:16px;border:1px solid #bbb;display:flex;align-items:center;justify-content:center}
.products{left:98px;top:558px;width:694px;display:flex;justify-content:space-between}
.product{width:173px;text-align:center;font-size:10px;color:#444}
.product-shot{width:112px;height:92px;margin:0 auto 18px;border-radius:8px 8px 30px 30px}
.product-price{margin-top:1px}

/* promos */
.promo{top:755px;width:221px;height:149px}
.promo-band{left:0;bottom:0;width:100%;height:42px;background:rgba(0,0,0,.6);color:#fff;display:flex;align-items:center;justify-content:center;gap:6px}
.promo-big{font-size:17px;font-weight:700}
.promo-small{font-size:8px}

/* footer */
.footer{left:0;top:962px;width:890px;height:238px;background:var(--footer)}
.footer-rule{left:0;top:1133px;width:890px;height:1px;background:var(--line)}
.f-head{font-size:12px;color:#222;font-weight:400}
.links{display:flex;gap:0}
.links ul{list-style:none;font-size:7.4px;color:#444;line-height:16.6px}
.links li::before{content:"•";margin-right:5px}
.field{width:156px;height:28px;border:1px solid #ccc;background:#fff;font-size:7.4px;color:#888;padding-left:11px;line-height:26px}
.subscribe{width:65px;height:27px;background:var(--dark);color:#fff;font-size:9px;text-align:center;line-height:27px}
.social{width:28px;height:28px}
.legal{left:169px;top:1153px;font-size:7.6px;color:#444;line-height:16.5px}
.foot-brand{left:98px;top:1152px;font-size:11px;font-weight:700;color:#888;display:flex;align-items:center;gap:4px}
.card{top:1158px;width:30px;height:20px;background:#8a8a8a;border-radius:2px}
</style>
</head>
<body>

<div class="abs topbar"></div>
<div class="abs phone">
  <svg width="14" height="14" viewBox="0 0 24 24" fill="none" stroke="#777" stroke-width="1.6"><path d="M5 3h4l2 5-3 2a12 12 0 0 0 6 6l2-3 5 2v4a2 2 0 0 1-2 2A17 17 0 0 1 3 5a2 2 0 0 1 2-2z"/></svg>
  555 017 4482
</div>
<div class="abs util">
  <svg width="16" height="17" viewBox="0 0 24 24" fill="none" stroke="#666" stroke-width="1.5"><circle cx="12" cy="8" r="4.5"/><path d="M3 22c0-5 4-8 9-8s9 3 9 8z"/></svg>
  <svg width="17" height="17" viewBox="0 0 24 24" fill="none" stroke="#666" stroke-width="1.8"><circle cx="10" cy="10" r="6.5"/><path d="M15 15l7 7"/></svg>
  <div style="display:flex;align-items:center;gap:6px">
    <div class="cart-label">My Cart<br><span style="font-size:8px">$00.00</span></div>
    <svg width="12" height="16" viewBox="0 0 16 20" fill="none" stroke="#666" stroke-width="1.4"><rect x="1" y="6" width="14" height="13"/><path d="M5 6V4a3 3 0 0 1 6 0v2"/></svg>
  </div>
</div>

<div class="abs header"></div>
<div class="abs figure" style="left:26px;top:48px;width:46px;height:142px" role="img" aria-label="Faint grey devil-girl silhouette decoration"></div>
<div class="abs figure" style="left:818px;top:82px;width:50px;height:108px" role="img" aria-label="Faint grey devil-girl silhouette decoration"></div>
<div class="abs brand"><span class="brand-dot"></span><span class="brand-name">Rex's Briefs</span></div>

<nav class="abs nav">
  <span class="current">Home</span>
  <span>Dangerous Rex’s</span>
  <span>Wild Rex’s</span>
  <span>Plain Rex’s</span>
  <span>All the Damn Rex’s</span>
  <span>Design Rex’s</span>
  <span>Rex’s Life</span>
  <span>Rex’s Jokes</span>
  <span>About Rex’s</span>
</nav>

<div class="abs hero" role="img" aria-label="Graffiti-covered alleyway tunnel in vivid orange, purple and red"></div>
<div class="abs hero-title">Aliquam lacinia dapibus nisi, in ullamcorper</div>
<div class="abs hero-cta">SHOP NOW</div>
<div class="abs hero-arrow" style="left:0"><svg width="8" height="12" viewBox="0 0 8 12" fill="none" stroke="#fff" stroke-width="1.3"><path d="M7 1L2 6l5 5"/></svg></div>
<div class="abs hero-arrow" style="right:0"><svg width="8" height="12" viewBox="0 0 8 12" fill="none" stroke="#fff" stroke-width="1.3"><path d="M1 1l5 5-5 5"/></svg></div>

<div class="abs section-head">
  <span class="pager"><svg width="6" height="9" viewBox="0 0 6 9" fill="none" stroke="#777"><path d="M5 1L1.5 4.5 5 8"/></svg></span>
  <span class="section-title">OUR PRODUCTS</span>
  <span class="pager"><svg width="6" height="9" viewBox="0 0 6 9" fill="none" stroke="#777"><path d="M1 1l3.5 3.5L1 8"/></svg></span>
</div>

<div class="abs products">
  <div class="product"><div class="product-shot" style="background:linear-gradient(135deg,#e0602a,#7a1e2a)" role="img" aria-label="Boxer briefs with red and orange swirl print"></div>Aliquam nulla risus rhoncus<div class="product-price">$00.00</div></div>
  <div class="product"><div class="product-shot" style="background:linear-gradient(135deg,#7a3bb8,#c8344a)" role="img" aria-label="Boxer briefs with purple octopus graffiti print"></div>Aliquam nulla risus rhoncus<div class="product-price">$00.00</div></div>
  <div class="product"><div class="product-shot" style="background:linear-gradient(180deg,#a6e22e 0 14%,#2a2a2a 14%)" role="img" aria-label="Plain black boxer briefs with lime waistband"></div>Aliquam nulla risus rhoncus<div class="product-price">$00.00</div></div>
  <div class="product"><div class="product-shot" style="background:linear-gradient(135deg,#2f5fd6,#e0c43a)" role="img" aria-label="Boxer briefs with blue and yellow pattern"></div>Aliquam nulla risus rhoncus<div class="product-price">$00.00</div></div>
</div>

<div class="abs promo" style="left:98px;background:linear-gradient(135deg,#d83a9a,#2aa8e0 50%,#1c3f9a)" role="img" aria-label="Blue and pink graffiti wall">
  <div class="abs promo-band"><span class="promo-big">$00.00</span><span class="promo-small">Morbi pellentesque nibh eget</span></div>
</div>
<div class="abs promo" style="left:334px;background:linear-gradient(135deg,#c9c2b0,#3ab0c8 45%,#c8342a)" role="img" aria-label="Wall of torn street posters">
  <div class="abs promo-band"><span class="promo-big">32%</span><span class="promo-small">Aliquam lacinia dapibus</span></div>
</div>
<div class="abs promo" style="left:571px;background:linear-gradient(135deg,#e0307a,#f0d02a 50%,#2a8a4a)" role="img" aria-label="Pink, yellow and green graffiti lettering">
  <div class="abs promo-band"><span class="promo-big" style="letter-spacing:.5px">FESTIVAL OFFER</span></div>
</div>

<div class="abs footer"></div>
<div class="abs figure" style="left:20px;top:1080px;width:56px;height:50px" role="img" aria-label="Faint grey reclining devil-girl silhouette decoration"></div>
<div class="abs figure" style="left:814px;top:1084px;width:66px;height:46px" role="img" aria-label="Faint grey reclining devil-girl silhouette decoration"></div>

<div class="abs f-head" style="left:98px;top:994px">Links</div>
<div class="abs links" style="left:98px;top:1017px">
  <ul style="width:107px"><li>Home</li><li>Dangerous Rex’s</li><li>Wild Rex’s</li><li>Plain Rex’s</li><li>All the Damn Rex’s</li></ul>
  <ul style="width:100px"><li>Design Rex’s</li><li>Rex’s Life</li><li>Rex’s Jokes</li><li>About Rex’s</li><li>My Account</li></ul>
  <ul><li>My Cart</li><li>Checkout</li><li>Wish list</li><li>Returns</li><li>Customer Care</li></ul>
</div>

<div class="abs f-head" style="left:430px;top:994px">Newsletter Subscribe</div>
<div class="abs field" style="left:430px;top:1021px">Full Name</div>
<div class="abs field" style="left:430px;top:1056px">Email Address</div>
<div class="abs subscribe" style="left:591px;top:1057px">Subscribe</div>

<div class="abs f-head" style="left:719px;top:994px">Social Media</div>
<div class="abs social" style="left:720px;top:1022px;background:#3b5a9a"></div>
<div class="abs social" style="left:755px;top:1022px;background:#2aa3e0"></div>

<div class="abs footer-rule"></div>
<div class="abs foot-brand"><span>Rex's Briefs</span></div>
<div class="abs legal">Copyright © 2016 Company name.<br>All rights reserved.</div>
<div class="abs card" style="left:666px"></div>
<div class="abs card" style="left:698px"></div>
<div class="abs card" style="left:730px"></div>
<div class="abs card" style="left:762px"></div>

</body>
</html>
```